ZORM Design tag

Looking to design a tag for our new hat & glove brand ZORM Design. These are winter hats & gloves. Long story short these are lower cost/retail items but I'm trying to convey higher quality goods through a nice tag. I’ve attached a tag of another brand we have to give you a general idea of what I’d be looking for- but again for our new brand ZORM Design.
I’m thinking we can do one general design- and then do it in 4 different color schemes: First one mimicking the attachment’s colors for ladies items- so a few different shades of pink. Then 2nd color scheme a darker more masculine color tone for mens or unisex items- maybe blue/dark blue, and then a 3rd color scheme for kids items that is more vibrant/kid like colors. Last one red & green for some Christmas items we do.
A few things:
• Trying to make the tags look classy as possible
• The tag will need to measure 2.25” high x 2” wide. The top little bit would have to be space left blank for a hole punch- just like on the attached sample tag. But again the tags designed would need to be 2.25" tall x 2" wide so not the same shape as the sample tag.
• For item name you can just put “Knit Hat” for the generic tag item name (in place of what says on the same “Chenille Slipper Bootie”). Please try to keep the writing a nice font similar to what is on this tag- again trying to have a classy tag look
• On the bottom center (In place of Made in China) it would just need to say “One Size” in standard font
Hope this helps & thank you
People buying winter hats & gloves
Retail- winter hats & gloves

```html
<!DOCTYPE html>
<html lang="en">
<head>
<meta charset="utf-8">
<title>ZORM Design – Knit Hat Tags</title>
<link rel="stylesheet" href="https://fonts.googleapis.com/css2?family=Montserrat:wght@500;600&family=Great+Vibes&display=swap">
<style>
  :root {
    --canvas-bg: #ffffff;
    --ink: #ffffff;
    --hole-shadow: #8a8a8a;

    --ladies-field-a: #fb7fb8;
    --ladies-field-b: #f75fa6;
    --ladies-band: #ff2a93;

    --mens-field-a: #0a50e0;
    --mens-field-b: #0338c8;
    --mens-band: #083594;

    --kids-field-a: #ffc21a;
    --kids-field-b: #ffad00;
    --kids-band: #ff5e00;

    --holiday-field-a: #d10f0f;
    --holiday-field-b: #b80606;
    --holiday-band: #0e5704;
  }

  html, body {
    margin: 0;
    padding: 0;
    width: 1200px;
    height: 1000px;
    overflow: hidden;
    background: var(--canvas-bg);
  }

  .tag-sheet {
    position: relative;
    width: 1200px;
    height: 1000px;
  }

  .tag {
    position: absolute;
    width: 359px;
    height: 404px;
    overflow: hidden;
    color: var(--ink);
  }
  .tag--ladies  { left: 225px; top: 78px;  --field-a: var(--ladies-field-a);  --field-b: var(--ladies-field-b);  --band: var(--ladies-band); }
  .tag--mens    { left: 617px; top: 78px;  --field-a: var(--mens-field-a);    --field-b: var(--mens-field-b);    --band: var(--mens-band); }
  .tag--kids    { left: 225px; top: 519px; --field-a: var(--kids-field-a);    --field-b: var(--kids-field-b);    --band: var(--kids-band); }
  .tag--holiday { left: 617px; top: 519px; --field-a: var(--holiday-field-a); --field-b: var(--holiday-field-b); --band: var(--holiday-band); }

  .tag__field {
    position: absolute;
    inset: 0;
    background: linear-gradient(135deg, var(--field-a), var(--field-b));
  }

  .tag__hole {
    position: absolute;
    left: 166px;
    top: 21px;
    width: 28px;
    height: 28px;
  }

  .tag__band {
    position: absolute;
    left: 0;
    top: 59px;
    width: 100%;
    height: 149px;
    background: var(--band);
    display: flex;
    flex-direction: column;
    align-items: center;
    justify-content: center;
    font-family: "Montserrat", sans-serif;
    font-weight: 600;
    line-height: 1;
  }
  .brand-name__main {
    font-size: 84px;
    letter-spacing: 2px;
  }
  .brand-name__sub {
    margin-top: 6px;
    font-size: 34px;
    letter-spacing: 16px;
    padding-left: 16px;
  }

  .tag__item {
    position: absolute;
    margin: 0;
    left: 0;
    top: 240px;
    width: 100%;
    text-align: center;
    white-space: nowrap;
    font-family: "Great Vibes", cursive;
    font-size: 84px;
    line-height: 84px;
  }

  .tag__size {
    position: absolute;
    margin: 0;
    left: 0;
    top: 355px;
    width: 100%;
    text-align: center;
    white-space: nowrap;
    font-family: "Montserrat", sans-serif;
    font-weight: 500;
    font-size: 17px;
    line-height: 17px;
    letter-spacing: 2px;
  }
</style>
</head>
<body>
<main class="tag-sheet">

  <article class="tag tag--ladies">
    <div class="tag__field" role="img" aria-label="Pink diamond pattern background"></div>
    <svg class="tag__hole" viewBox="0 0 28 28" aria-hidden="true">
      <circle cx="14" cy="14" r="13" fill="#ffffff"/>
      <path d="M5 16 L14 24 L23 16 Z" fill="var(--hole-shadow)"/>
    </svg>
    <header class="tag__band brand-name">
      <span class="brand-name__main">ZORM</span>
      <span class="brand-name__sub">DESIGN</span>
    </header>
    <p class="tag__item">Knit Hat</p>
    <p class="tag__size">ONE SIZE</p>
  </article>

  <article class="tag tag--mens">
    <div class="tag__field" role="img" aria-label="Blue diamond pattern background"></div>
    <svg class="tag__hole" viewBox="0 0 28 28" aria-hidden="true">
      <circle cx="14" cy="14" r="13" fill="#ffffff"/>
      <path d="M5 16 L14 24 L23 16 Z" fill="var(--hole-shadow)"/>
    </svg>
    <header class="tag__band brand-name">
      <span class="brand-name__main">ZORM</span>
      <span class="brand-name__sub">DESIGN</span>
    </header>
    <p class="tag__item">Knit Hat</p>
    <p class="tag__size">ONE SIZE</p>
  </article>

  <article class="tag tag--kids">
    <div class="tag__field" role="img" aria-label="Yellow diamond pattern background"></div>
    <svg class="tag__hole" viewBox="0 0 28 28" aria-hidden="true">
      <circle cx="14" cy="14" r="13" fill="#ffffff"/>
      <path d="M5 16 L14 24 L23 16 Z" fill="var(--hole-shadow)"/>
    </svg>
    <header class="tag__band brand-name">
      <span class="brand-name__main">ZORM</span>
      <span class="brand-name__sub">DESIGN</span>
    </header>
    <p class="tag__item">Knit Hat</p>
    <p class="tag__size">ONE SIZE</p>
  </article>

  <article class="tag tag--holiday">
    <div class="tag__field" role="img" aria-label="Red diamond pattern background"></div>
    <svg class="tag__hole" viewBox="0 0 28 28" aria-hidden="true">
      <circle cx="14" cy="14" r="13" fill="#ffffff"/>
      <path d="M5 16 L14 24 L23 16 Z" fill="var(--hole-shadow)"/>
    </svg>
    <header class="tag__band brand-name">
      <span class="brand-name__main">ZORM</span>
      <span class="brand-name__sub">DESIGN</span>
    </header>
    <p class="tag__item">Knit Hat</p>
    <p class="tag__size">ONE SIZE</p>
  </article>

</main>
</body>
</html>
```